Book cover - Rise Above Unease and Bashful Nerves

Book cover for Ebook (Lumora) and wrap around print cover (Printvale) (back, front, and spine)

The book title (may slightly change by end of brief):
(MAIN TITLE) 'Rise Above Unease and Bashful Nerves'
(SUB HEADING) 'A Clear Daily Workbook Guide to Rise Above Unease, Outgrow Timidity and Build Inner Poise'
by Dr Owen Farrby

I would like a bold, stand out cover. Contemporary. I would like to avoid stereotypical images of people looking anxious or worried. I would like the design to be more uplifting and hopeful, rather than focusing on the negative aspect of anxiety, but avoiding cliched photos of people raising their hands in the air, smiling and jumping etc. The cover should appeal to both men and women.

Trim size of book cover (for PrintVale) is 5.25" x 8" back and front with a spine size of 0.477 inches

Reason: I have decided to extend the deadline by 1 more day, not because I am unhappy with the quality of the designs, but because a few designers have contacted me to explain they have had technical difficulties when submitting their files. Thanks everyone for the hard work and great designs.

Target Market(s)

Males and females (16+) who struggle with social anxiety and shyness

Industry/Entity Type

Social

Font styles to use
Serif

Requirements
Must have
• Bold cover that is modern and contemporary. For example, I like these covers:
• http://qvlk.io/8kTz3Pm
• http://qvlk.io/9wHe5Nb
• http://qvlk.io/4jMr7Yc
• http://qvlk.io/6nGs2Lq
• http://qvlk.io/3fVb81t
• http://qvlk.io/7yKd4Ue
• http://qvlk.io/5hWx9Oa
Nice to have
• Open to abstract designs.
Should not have
• No stereotypical pictures of people who look anxious or worried. Avoid cliched photos of people raising their hands in the air, smiling and jumping etc.

```html
<!DOCTYPE html>
<html lang="en">
<head>
<meta charset="utf-8">
<title>Rise Above Unease and Bashful Nerves — Book Cover</title>
<link rel="stylesheet" href="https://fonts.googleapis.com/css2?family=Arimo:wght@400&display=swap">
<style>
  :root {
    --ink: #0d0d0d;
    --ember: #c8521a;
    --lavender: #b3a6f2;
    --paper: #fbf6ea;
    --author: #2b2b2b;
    --sky-slate: #8fa3b4;
    --sunset: #d9702a;
    --dusk-blue: #9fb3d8;
    --sand: #c9a47e;
  }
  * { margin: 0; padding: 0; box-sizing: border-box; }
  html, body {
    width: 788px; height: 1200px; overflow: hidden;
    background: #ffffff;
  }
  .cover {
    position: relative;
    width: 788px; height: 1200px;
    overflow: hidden;
    font-family: "Arimo", Arial, sans-serif;
    text-align: center;
  }
  .cover-art {
    position: absolute; inset: 0;
    background:
      radial-gradient(ellipse 62% 30% at 50% 60%, rgba(255,252,242,0.98) 0%, rgba(255,250,235,0.85) 45%, rgba(255,248,230,0) 100%),
      radial-gradient(ellipse 55% 40% at 92% 8%, var(--sunset) 0%, rgba(226,140,60,0.75) 40%, rgba(240,190,110,0) 80%),
      radial-gradient(ellipse 55% 40% at 6% 12%, var(--sky-slate) 0%, rgba(170,180,180,0.6) 45%, rgba(200,200,190,0) 85%),
      radial-gradient(ellipse 45% 30% at 15% 92%, var(--dusk-blue) 0%, rgba(170,190,225,0.5) 55%, rgba(200,210,230,0) 100%),
      radial-gradient(ellipse 50% 30% at 60% 88%, var(--sand) 0%, rgba(210,180,150,0.5) 50%, rgba(230,210,190,0) 100%),
      radial-gradient(ellipse 40% 30% at 95% 80%, #a9b8dc 0%, rgba(190,200,230,0) 100%),
      linear-gradient(180deg, #d9c49a 0%, #efe2c4 35%, #f6efe0 55%, #d7cfd6 80%, #bfc5d9 100%);
  }
  .title {
    position: absolute; left: 0; right: 0;
    font-weight: 400; line-height: 1; white-space: nowrap;
    letter-spacing: 0.01em;
  }
  .title-line-1 { top: 412px; font-size: 100px; color: var(--ink); }
  .title-line-2 { top: 528px; font-size: 78px; color: var(--ember); }
  .title-line-3 { top: 628px; font-size: 62px; color: var(--ink); }
  .title-line-3 .accent { color: var(--lavender); }
  .subtitle {
    position: absolute; left: 90px; right: 90px; top: 736px;
    font-size: 22px; line-height: 1.36; color: #ffffff;
    text-shadow: 0 0 3px rgba(0,0,0,0.55), 0 1px 2px rgba(0,0,0,0.45);
  }
  .author {
    position: absolute; left: 0; right: 0; top: 1136px;
    font-size: 34px; color: var(--author);
  }
</style>
</head>
<body>
  <main class="cover">
    <div class="cover-art" role="img" aria-label="Abstract watercolour wash in slate blue, warm orange and cream with glowing white light lines"></div>
    <h1>
      <span class="title title-line-1">RISE ABOVE</span>
      <span class="title title-line-2">UNEASE</span>
      <span class="title title-line-3">AND <span class="accent">BASHFUL NERVES</span></span>
    </h1>
    <p class="subtitle">A Clear Daily Workbook Guide to Rise Above Unease, Outgrow Timidity and Build Inner Poise</p>
    <p class="author">Dr Owen Farrby</p>
  </main>
</body>
</html>
```